Pharmacy

Two sided postcard. Pictures on one side. Description on the other. We design and build pharmacies. pictures are some of our finished work. You can use as many pictures as you like not necessary to use all of them. Size of card should be 5"x7". See my website at display@brightfieldfixtures.com for more inspiration. I include the back of one card that I used recently. Both sids need design input. Feel free to contact me with questions.
Requirements
Must have
- Must be a two sided postcard
Nice to have
- I am sending a design of a sleek type postcard that I saw online as an example.
- https://lnk.example-pics.net/images/q7KmRz
- I am looking for something modern.
- Not limited to colors on my website.

```html
<!DOCTYPE html>
<html lang="en">
<head>
<meta charset="utf-8">
<title>Brightfield Showcase – Postcard</title>
<link rel="stylesheet" href="https://fonts.googleapis.com/css2?family=Cinzel:wght@600;700&family=Oswald:wght@300;500;600&family=Open+Sans:wght@400;700&display=swap">
<style>
  :root {
    --stage: #3b3c3e;
    --card: #ffffff;
    --brand-red: #7d1315;
    --panel-dark: #2f3133;
    --panel-mid: #4a4c4f;
    --band-grey: #a1a4a8;
    --body-tint: #d9e0e7;
    --ink: #2b2b2b;
    --accent-gold: #f2a531;
    --white: #ffffff;
  }
  * { margin: 0; padding: 0; box-sizing: border-box; }
  html, body { width: 1000px; height: 1200px; overflow: hidden; }
  body { background: var(--stage); position: relative; font-family: "Open Sans", Arial, sans-serif; }

  .postcard { position: absolute; left: 106px; width: 739px; height: 462px; overflow: hidden; background: var(--card); box-shadow: 0 10px 24px rgba(0,0,0,.45); }
  .postcard--front { top: 105px; }
  .postcard--back { top: 641px; }

  .front-art { position: absolute; inset: 0; }

  .tilted { position: absolute; transform-origin: left top; transform: rotate(-6deg); }
  .front-title {
    left: 64px; top: 226px; color: var(--white);
    font-family: "Cinzel", Georgia, serif; font-weight: 700;
    font-size: 37px; line-height: 38px; letter-spacing: .5px;
    text-align: center; width: 620px;
  }
  .front-tagline {
    left: 378px; top: 292px; color: var(--white);
    font-family: "Oswald", Arial, sans-serif; font-weight: 600;
    font-size: 19px; line-height: 20px; text-align: center; width: 300px; letter-spacing: .4px;
  }
  .service-list {
    left: 386px; top: 345px; list-style: none; color: var(--white);
    font-family: "Oswald", Arial, sans-serif; font-weight: 500; font-size: 18px; line-height: 20px;
  }
  .service-list li { display: flex; align-items: center; gap: 7px; }
  .service-list svg { width: 14px; height: 12px; flex: none; }
  .since-tag {
    left: 601px; top: 322px; background: var(--accent-gold); color: var(--panel-dark);
    font-family: "Oswald", Arial, sans-serif; font-weight: 600; font-size: 13px;
    padding: 1px 10px; transform: rotate(-6deg) skewX(-12deg);
  }
  .call-cta {
    left: 566px; top: 355px; color: var(--white); font-family: "Oswald", Arial, sans-serif;
  }
  .call-cta__label { font-weight: 300; font-size: 17px; line-height: 20px; }
  .call-cta__phone { font-weight: 500; font-size: 22px; line-height: 26px; }

  .about-panel { position: absolute; left: 41px; top: 36px; width: 328px; }
  .about-panel__head {
    background: var(--brand-red); color: var(--white); height: 74px;
    font-family: "Cinzel", Georgia, serif; font-weight: 600; font-size: 17.5px; line-height: 24px;
    text-align: center; padding-top: 12px;
  }
  .about-panel__motto {
    background: var(--band-grey); color: var(--brand-red); height: 35px; line-height: 35px;
    font-family: "Cinzel", Georgia, serif; font-weight: 700; font-size: 11.5px; text-align: center; letter-spacing: .4px;
  }
  .about-panel__body {
    background: var(--body-tint); height: 221px; padding: 20px 27px 0;
    color: var(--ink); font-size: 13.3px; line-height: 17.5px; text-align: justify;
  }
  .about-panel__body p + p { margin-top: 8px; }
  .about-panel__phone {
    background: var(--brand-red); color: var(--white); height: 30px; line-height: 30px;
    text-align: center; font-size: 18px; font-weight: 700; letter-spacing: .5px;
  }
  .about-panel__email { color: var(--brand-red); text-align: center; font-size: 13px; line-height: 17px; margin-top: 1px; }
  .about-panel__web { color: var(--brand-red); text-align: center; font-size: 19px; font-weight: 700; line-height: 22px; }

  .return-address { position: absolute; left: 387px; top: 48px; color: var(--ink); font-size: 10px; line-height: 11px; font-style: normal; }
  .postage-indicia {
    position: absolute; left: 600px; top: 39px; width: 87px; height: 83px;
    border: 1.5px solid var(--ink); color: var(--ink); font-size: 10px; line-height: 13px;
    text-align: center; padding-top: 8px;
  }
</style>
</head>
<body>

<section class="postcard postcard--front" aria-label="Postcard front">
  <svg class="front-art" viewBox="0 0 739 462" width="739" height="462">
    <defs>
      <linearGradient id="photoPharmacyA" x1="0" y1="0" x2="1" y2="1">
        <stop offset="0" stop-color="#d7d9dc"/><stop offset=".6" stop-color="#7c8596"/><stop offset="1" stop-color="#5d6066"/>
      </linearGradient>
      <linearGradient id="photoPharmacyB" x1="0" y1="0" x2="1" y2="1">
        <stop offset="0" stop-color="#c9b79d"/><stop offset=".5" stop-color="#7a4a34"/><stop offset="1" stop-color="#d6cbc0"/>
      </linearGradient>
      <linearGradient id="photoPharmacyC" x1="0" y1="0" x2="1" y2="1">
        <stop offset="0" stop-color="#e3e4e0"/><stop offset=".5" stop-color="#9b6a45"/><stop offset="1" stop-color="#6a3e24"/>
      </linearGradient>
      <linearGradient id="slatePanel" x1="0" y1="0" x2="1" y2="1">
        <stop offset="0" stop-color="#1f2022"/><stop offset=".6" stop-color="#4f5255"/><stop offset="1" stop-color="#3a3c3f"/>
      </linearGradient>
    </defs>
    <rect x="0" y="0" width="370" height="260" fill="url(#photoPharmacyA)" role="img" aria-label="Photo of a finished pharmacy interior with white and dark shelving"/>
    <rect x="357" y="0" width="382" height="210" fill="url(#photoPharmacyB)" role="img" aria-label="Photo of a cosmetics store with wood cabinets and glass display counters"/>
    <rect x="0" y="260" width="330" height="202" fill="url(#photoPharmacyC)" role="img" aria-label="Photo of pharmacy aisle with wooden end-cap shelving"/>
    <polygon points="318,270 739,226 739,462 318,462" fill="url(#slatePanel)"/>
    <polygon points="0,228 739,150 739,240 0,318" fill="var(--brand-red)"/>
    <polygon points="420,462 739,395 739,462" fill="var(--brand-red)"/>
  </svg>

  <div class="tilted front-title">Brightfield Showcase &amp;<br>Store Fixture Co Inc.</div>
  <div class="tilted front-tagline">A COMPLETE SERVICE FROM DESIGN<br>THRU INSTALLATION</div>
  <div class="tilted since-tag">Since 1917</div>
  <ul class="tilted service-list">
    <li><svg viewBox="0 0 14 12"><path d="M1 6 L5 10 L13 2" stroke="#c0282c" stroke-width="3" fill="none"/></svg>Pharmacies</li>
    <li><svg viewBox="0 0 14 12"><path d="M1 6 L5 10 L13 2" stroke="#c0282c" stroke-width="3" fill="none"/></svg>Jewelry Stores</li>
    <li><svg viewBox="0 0 14 12"><path d="M1 6 L5 10 L13 2" stroke="#c0282c" stroke-width="3" fill="none"/></svg>Vintage Stores</li>
    <li><svg viewBox="0 0 14 12"><path d="M1 6 L5 10 L13 2" stroke="#c0282c" stroke-width="3" fill="none"/></svg>Other Stores</li>
    <li><svg viewBox="0 0 14 12"><path d="M1 6 L5 10 L13 2" stroke="#c0282c" stroke-width="3" fill="none"/></svg>Prefabricated</li>
  </ul>
  <div class="tilted call-cta">
    <div class="call-cta__label">GIVE US A CALL AT</div>
    <div class="call-cta__phone">201 555 0148</div>
  </div>
</section>

<section class="postcard postcard--back" aria-label="Postcard back">
  <div class="about-panel">
    <div class="about-panel__head">Brightfield Showcase &amp;<br>Store Fixture Co Inc.</div>
    <div class="about-panel__motto">Quality - Experience - Innovation</div>
    <div class="about-panel__body">
      <p>Family owned and operated for three generations Brightfield Showcase &amp; Store Fixture Co. Inc is the oldest store fixture company in New Jersey.</p>
      <p>As designers &amp; Manufacturers we can save you hours of time and money.</p>
      <p>Our level of experience will be evident from the outset and you will be pleased that you found us.</p>
    </div>
    <div class="about-panel__phone">201 555 0148</div>
    <div class="about-panel__email">display@brightfieldfixtures.com</div>
    <div class="about-panel__web">www.brightfieldfixtures.com</div>
  </div>

  <address class="return-address">
    Brightfield Showcase &amp;<br>Store Fixture Co. Inc.<br>PO BOX 318<br>Ridgefield NJ 07657
  </address>

  <div class="postage-indicia">presorted<br>FIRST CLASS<br>US POSTAGE<br>PAID<br>MAILPOINT</div>
</section>

</body>
</html>
```